TOLO Electrical Services Letter Head

I need a professional clean looking design that will incorporate my company logo and information such as postal address, website, contact email "service@tolovoltworks.com.au" and phone number.

somewhere on the document i will also require my electrical contractor number "EC 046215" and my Australian Business number "57 139 604 282" these have to legally be on the document so they dont need to be a main feature, maybe in the footer in a smaller text.

Can you also have the 3 blue dashes from my logo as the watermark.

I would like the colour scheme to match my logo, business card and website www.tolovoltworks.com.au

I have the JPEG and PNG files for my logo which it will not allow me to upload as they are too wide, if you require these please let me know.

Target Market(s)

To be used for quotes and letters to commercial clients

Industry/Entity Type

Electric Company

Colors
0555a3
3176b5
85acd3
cfdfed
eaf1f7

Requirements
Must have
• company logo and information such as postal address, website, contact email "service@tolovoltworks.com.au" and phone number.
• somewhere on the document i will also require my electrical contractor number "EC 046215" and my Australian Business number "57 139 604 282" these have to legally be on the document so they dont need to be a main feature, maybe in the footer in a smaller text.
• I would like the colour scheme to match my logo, business card and website www.tolovoltworks.com.au
Nice to have
• Can you also have the 3 blue dashes from my logo as the watermark.

```html
<!DOCTYPE html>
<html lang="en">
<head>
<meta charset="utf-8">
<title>TOLO Electrical Services – Letterhead</title>
<link rel="stylesheet" href="https://fonts.googleapis.com/css2?family=Open+Sans:wght@400;700&display=swap">
<style>
  :root {
    --brand-deep: #0555a3;
    --brand-mid: #3176b5;
    --brand-sky: #29abe2;
    --brand-pale: #85acd3;
    --brand-mist: #cfdfed;
    --brand-ice: #eaf1f7;
    --paper: #fafcfd;
    --ink: #111111;
    --text-grey: #4a4a4a;
  }
  * { margin: 0; padding: 0; box-sizing: border-box; }
  html, body {
    width: 927px;
    height: 1200px;
    overflow: hidden;
    background: var(--paper);
  }
  .letterhead {
    position: relative;
    width: 927px;
    height: 1200px;
    background: var(--paper);
    font-family: "Open Sans", Arial, sans-serif;
    overflow: hidden;
  }
  .brand {
    position: absolute;
    left: 53px;
    top: 78px;
    display: flex;
    align-items: center;
    gap: 14px;
  }
  .brand-mark {
    width: 22px;
    height: 22px;
    background: var(--brand-mid);
  }
  .brand-name {
    font-size: 34px;
    font-weight: 700;
    color: var(--ink);
    letter-spacing: 0.2px;
  }
  .contact {
    position: absolute;
    right: 77px;
    top: 46px;
    text-align: right;
    font-style: normal;
    font-size: 15.5px;
    line-height: 23.5px;
    color: var(--text-grey);
  }
  .contact-company {
    font-size: 18px;
    font-weight: 700;
    color: var(--brand-mid);
    line-height: 26px;
  }
  .contact-line {
    display: flex;
    justify-content: flex-end;
    align-items: center;
    gap: 5px;
  }
  .contact-icon {
    width: 12px;
    height: 12px;
    flex: none;
  }
  .watermark {
    position: absolute;
    left: 152px;
    top: 510px;
    width: 623px;
    height: 172px;
    display: flex;
    align-items: center;
    justify-content: center;
    font-size: 52px;
    font-weight: 700;
    color: var(--brand-ice);
    white-space: nowrap;
  }
  .legal {
    position: absolute;
    left: 0;
    bottom: 80px;
    width: 927px;
    text-align: center;
    font-size: 12px;
    line-height: 16px;
    color: var(--text-grey);
    letter-spacing: 0.3px;
  }
  .legal-sep {
    color: var(--brand-pale);
    margin: 0 10px;
  }
  .footer-band {
    position: absolute;
    left: 0;
    bottom: 3px;
    width: 927px;
    height: 66px;
    background: linear-gradient(90deg, var(--brand-sky), var(--brand-mid) 45%, var(--brand-deep));
  }
</style>
</head>
<body>
<main class="letterhead">
  <header>
    <div class="brand">
      <span class="brand-mark"></span>
      <span class="brand-name">TOLO Electrical Services</span>
    </div>
    <address class="contact">
      <div class="contact-company">TOLO Electrical Services</div>
      <div>P.O Box 2819, Harbour Ridge</div>
      <div>WA 6032</div>
      <div class="contact-line">(08) 6120 4471
        <svg class="contact-icon" viewBox="0 0 12 12" aria-hidden="true"><path d="M2.5 1 L4.5 1 L5.2 3.6 L4 4.6 C4.6 6 5.8 7.3 7.4 8 L8.4 6.8 L11 7.5 L11 9.5 C11 10.3 10.3 11 9.5 11 C5 11 1 7 1 2.5 C1 1.7 1.7 1 2.5 1 Z" fill="var(--brand-mid)"/></svg>
      </div>
      <div class="contact-line">service@tolovoltworks.com.au
        <svg class="contact-icon" viewBox="0 0 12 12" aria-hidden="true"><rect x="1" y="2.5" width="10" height="7" rx="1" fill="none" stroke="var(--brand-mid)" stroke-width="1.3"/><path d="M1.5 3 L6 6.5 L10.5 3" fill="none" stroke="var(--brand-mid)" stroke-width="1.3"/></svg>
      </div>
      <div class="contact-line">www.tolovoltworks.com.au
        <svg class="contact-icon" viewBox="0 0 12 12" aria-hidden="true"><circle cx="6" cy="6" r="5" fill="var(--brand-mid)"/><path d="M1 6 H11 M6 1 C3.5 3.5 3.5 8.5 6 11 M6 1 C8.5 3.5 8.5 8.5 6 11" fill="none" stroke="var(--paper)" stroke-width="0.9"/></svg>
      </div>
    </address>
  </header>

  <div class="watermark" aria-hidden="true">TOLO Electrical Services</div>

  <p class="legal">EC 046215<span class="legal-sep">|</span>ABN 57 139 604 282</p>

  <footer class="footer-band" role="img" aria-label="Decorative band of slanted blue stripes in the brand colours"></footer>
</main>
</body>
</html>
```